Packaging & Label Design for CDB Products

We are a European CBD company specialising in athletic recovery, sleep improvement and wellness.

We would like the packaging to incorporate our logo and name (and font 'Codec') 'Meridell CBD'. The design must be transferable to all of our products. CBD Oils, Balms, Lip Balm and Vape E-Liquid.

We would like it to be simple but eye-catching and modern. We don't want bright colours. Preferred pallet of muted greys, blacks, white and pastel colours. Geometric concepts, possibly using different colours for each item of the range, we are open to new and fresh ideas (we are seeking you for your experience) and when we find the right design we would likely throw more work in your direction..

Our product range is not complete so the designer must be flexible with some changes and provide files where format can be easily edited by packaging manufacturer. We are also waiting for dimensions for the labels and boxes for several products and will supply the designer with full dimensions of all products once selected.

Oil Box: 2.6 x 9.0 x 2.6 cm (open format 16.7 x 11.6cm)
Labels: 7.8 x 3.3 cm (Front and Back)

Our expected product range will be:
CBD Oil 1000mg
CBD Oil 3000mg
CBD Balm 100mg
CBD Balm 300mg
E-Liquid 500mg
Lip Balm 50mg

We look forward to seeing your ideas.

Best Regards
Meridell CBD

```html
<!DOCTYPE html>
<html lang="en">
<head>
<meta charset="utf-8">
<title>Meridell CBD – CBD Oil 1000mg Box Dieline</title>
<link rel="stylesheet" href="https://fonts.googleapis.com/css2?family=Alfa+Slab+One&family=Montserrat:wght@700&family=Oswald:wght@500&display=swap">
<style>
  :root {
    --paper: #ffffff;
    --board: #000000;
    --gold: #dcb66b;
    --gold-deep: #5a4a2b;
    --ink-light: #ffffff;
  }
  html, body {
    margin: 0;
    padding: 0;
    width: 867px;
    height: 1200px;
    overflow: hidden;
    background: var(--paper);
  }
  .dieline { display: block; width: 867px; height: 1200px; }
  .board { fill: var(--board); }
  .frame { fill: none; stroke: var(--gold); }
  .frame--outer { stroke-width: 1.6; }
  .frame--inner { stroke-width: 1; }
  .ornament { fill: var(--gold-deep); }
  .rule { stroke: var(--ink-light); stroke-width: 1.2; }
  .brand-name {
    font-family: "Montserrat", sans-serif;
    font-weight: 700;
    fill: var(--ink-light);
    letter-spacing: 1px;
  }
  .brand-name--panel { fill: var(--gold); letter-spacing: 3px; }
  .product-name {
    font-family: "Alfa Slab One", serif;
    fill: var(--gold);
  }
  .strength {
    font-family: "Oswald", sans-serif;
    font-weight: 500;
    fill: var(--ink-light);
  }
</style>
</head>
<body>
<svg class="dieline" viewBox="0 0 768 1062" xmlns="http://www.w3.org/2000/svg" role="img" aria-label="Meridell CBD oil box, flat dieline">
  <defs>
    <!-- Front label block, drawn at its own origin -->
    <g id="front-label">
      <!-- brand box -->
      <rect class="frame frame--outer" x="0" y="0" width="128" height="95"/>
      <rect class="frame frame--inner" x="4" y="4" width="120" height="87"/>
      <g role="img" aria-label="Art deco corner ornaments">
        <rect class="ornament" x="6" y="6" width="22" height="22"/>
        <rect class="ornament" x="100" y="6" width="22" height="22"/>
      </g>
      <text class="brand-name" x="64" y="82" font-size="14" text-anchor="middle">MERIDELL</text>

      <!-- product box -->
      <rect class="frame frame--outer" x="0" y="98" width="128" height="332"/>
      <rect class="frame frame--inner" x="10" y="108" width="108" height="312" rx="4"/>
      <text class="product-name" transform="translate(66,264) rotate(-90)" font-size="90"
            text-anchor="middle" dominant-baseline="central"
            textLength="282" lengthAdjust="spacingAndGlyphs">CBD OIL</text>

      <!-- strength box -->
      <rect class="frame frame--outer" x="0" y="433" width="128" height="82"/>
      <rect class="frame frame--inner" x="4" y="437" width="120" height="74"/>
      <g role="img" aria-label="Art deco corner ornaments">
        <rect class="ornament" x="6" y="487" width="22" height="22"/>
        <rect class="ornament" x="100" y="487" width="22" height="22"/>
      </g>
      <line class="rule" x1="26" y1="447" x2="42" y2="447"/>
      <line class="rule" x1="86" y1="447" x2="102" y2="447"/>
      <text class="strength" x="64" y="455" font-size="20" text-anchor="middle">1000</text>
      <text class="strength" x="64" y="479" font-size="20" text-anchor="middle">mg</text>
    </g>
  </defs>

  <!-- Box net -->
  <g class="box-net">
    <path class="board tuck-flap" d="M90,253 L90,75 Q90,45 120,45 L238,45 Q268,45 268,75 L268,253 Z"/>
    <path class="board dust-flap" d="M268,253 L268,155 Q268,143 280,143 L355,143 Q365,143 368,150 L400,235 L420,245 L420,253 Z"/>
    <path class="board dust-flap" d="M550,253 L550,245 L570,235 L600,150 Q603,143 612,143 L703,143 Q715,143 715,155 L715,253 Z"/>
    <rect class="board body" x="40" y="253" width="688" height="555" rx="8"/>
    <path class="board bottom-flap" d="M255,800 L365,800 L365,908 Q365,918 355,918 L265,918 Q255,918 255,908 Z"/>
    <path class="board bottom-tuck" d="M397,800 L575,800 L575,980 Q575,1015 540,1015 L432,1015 Q397,1015 397,980 Z"/>
    <path class="board bottom-flap" d="M575,800 L715,800 L715,908 Q715,918 705,918 L612,918 Q604,918 600,910 L575,850 Z"/>
  </g>

  <!-- Top tuck label, reads when closed -->
  <g class="tuck-label" transform="rotate(180 178.5 187.5)">
    <rect class="frame frame--outer" x="117" y="125" width="123" height="125"/>
    <rect class="frame frame--inner" x="121" y="129" width="115" height="117"/>
    <g role="img" aria-label="Art deco corner ornaments">
      <rect class="ornament" x="123" y="131" width="22" height="22"/>
      <rect class="ornament" x="212" y="131" width="22" height="22"/>
      <rect class="ornament" x="123" y="222" width="22" height="22"/>
      <rect class="ornament" x="212" y="222" width="22" height="22"/>
    </g>
    <text class="brand-name" x="178.5" y="193" font-size="14" text-anchor="middle">MERIDELL</text>
  </g>

  <!-- Front and back panels -->
  <use href="#front-label" transform="translate(115,280)"/>
  <use href="#front-label" transform="translate(422,280)"/>

  <!-- Side panel brand mark -->
  <text class="brand-name brand-name--panel" x="640" y="536" font-size="20" text-anchor="middle">MERIDELL</text>
</svg>
</body>
</html>
```